Larkfield Clinic Booklet 2016

Larkfield Clinic is a multi-specialty Practice in Midtown Manhattan offering advanced care in multiple areas of medicine. See our table of contents (PDF Uploaded)
Our designed booklet should be clean, easy to read, contemporary, high-end and elegant.
We need a general theme, Layout for cover and templates for internal.
We are entertaining the idea of two different sizes
8 x 10
or
11 x 8.5
Our tagline " The Future of Medicine is Here"
We will provide all the text content
The link to our website
www.LarkfieldCL.example
Uploaded files are as follows.. Logo, Our Team Photo and the PDF listing the table of contents.

```html
<!DOCTYPE html>
<html lang="en">
<head>
<meta charset="utf-8">
<title>Larkfield Clinic Booklet – Back Cover</title>
<link rel="stylesheet" href="https://fonts.googleapis.com/css2?family=Source+Sans+3:wght@400;600;700&display=swap">
<style>
  :root {
    --backdrop: #e4e4e4;
    --paper: #ffffff;
    --panel-grey: #c9c9c9;
    --panel-text: #ffffff;
    --divider: rgba(255,255,255,0.75);
    --dot-light: #f4f6f9;
    --dot-tone: #dde3ec;
    --accent-blue: #3d7fc4;
  }
  * { box-sizing: border-box; margin: 0; padding: 0; }
  html, body {
    width: 1200px; height: 900px; overflow: hidden;
    background: var(--backdrop);
    font-family: "Source Sans 3", "Helvetica Neue", Arial, sans-serif;
  }
  .back-cover {
    position: absolute; left: 100px; top: 64px;
    width: 1000px; height: 773px;
    background: var(--paper);
    box-shadow: 0 6px 24px rgba(0,0,0,0.12);
  }
  .contact-block {
    position: absolute; left: 400px; top: 400px;
    width: 600px; height: 367px;
  }
  .contact-band {
    height: 176px;
    background: var(--panel-grey);
    display: flex; align-items: stretch;
    color: var(--panel-text);
  }
  .contact-details {
    width: 300px; padding: 26px 0 0 34px;
    font-size: 15px; line-height: 1.3;
  }
  .contact-details h2 {
    font-size: 22px; font-weight: 700; margin-bottom: 4px;
  }
  .band-divider {
    width: 2px; margin: 28px 0 34px; background: var(--divider);
  }
  .call-us {
    padding: 70px 0 0 30px;
  }
  .call-us .label { font-size: 15px; font-weight: 600; }
  .call-us .phone {
    font-size: 34px; font-weight: 700; letter-spacing: 0.5px;
    text-shadow: 0 2px 4px rgba(0,0,0,0.25);
  }
  .dot-field {
    height: 191px;
    background: linear-gradient(180deg, var(--dot-light) 0%, var(--dot-tone) 100%);
  }
  .accent-rule {
    position: absolute; left: 400px; bottom: 0;
    width: 600px; height: 6px; background: var(--accent-blue);
  }
</style>
</head>
<body>
  <main class="back-cover">
    <section class="contact-block">
      <div class="contact-band">
        <address class="contact-details" style="font-style:normal">
          <h2>Contact Us</h2>
          <p>Larkfield Clinic</p>
          <p>140 E. 48th Street</p>
          <p>New York, NY 10017</p>
          <p>Fax: 212-555-0192</p>
        </address>
        <div class="band-divider"></div>
        <div class="call-us">
          <p class="label">Call Us</p>
          <p class="phone">212-555-0147</p>
        </div>
      </div>
      <div class="dot-field" role="img" aria-label="Soft halftone dot pattern fading from white to pale blue-grey"></div>
    </section>
    <div class="accent-rule"></div>
  </main>
</body>
</html>
```